Business Card & Logo Design Project

I am looking for a slick/simple design for a logo and business card, for a music Producer/Mixer/Engineer.

I'm based in Tokyo, Japan and I help my clients polish up their creation to major radio/TV status. My clients pay me for my taste, sense of balance expertise and creative direction/

Design should give impression of seal of quality, professionalism, and enthusiasm need some sort of a logo like design for "vantiri productions".

Please don't include music notes or instruments or anything musically related and anything samurai or ninja or too much Japan in them on the design.

I like clever, slick stuff that's not too obvious.
I also like a smooth gradation type transition. My favorite color is deep dark blue/

Good Luck and Thank you for your effort.
Updates

I would like a two-sided design for this one.
One side with "vantiri productions" (all lower case) on, and the other side with my name and contact info.

Please also consider portrait position (or direction).  (as opposed to landscape) 

Target Market(s)

My primary targets are artists & bands, who want absolute best for their creation.

Industry/Entity Type

Business

Requirements
Must have
• Two-Sided
1, vantiri productions
2, Kenji Matsuda, Producer/Mixer/Engineer, +81 090 4827 3516, brightwaver@mailbox-example.com
Nice to have
• Any suggestions are welcome//
Should not have
• Anything music related images.
(e.g. CD, music notations, instruments etc.)

```html
<!DOCTYPE html>
<html lang="en">
<head>
<meta charset="utf-8">
<title>vantiri productions — business card</title>
<link rel="stylesheet" href="https://fonts.googleapis.com/css2?family=Arimo:wght@400;700&display=swap">
<style>
  :root {
    --backdrop: #2a2a2a;
    --card-glow: #1b5676;
    --card-mid: #103a5a;
    --card-edge: #0a2643;
    --ink: #ffffff;
  }
  * { margin: 0; padding: 0; box-sizing: border-box; }
  html, body {
    width: 1200px;
    height: 900px;
    overflow: hidden;
    background: var(--backdrop);
    font-family: "Arimo", Arial, sans-serif;
    color: var(--ink);
  }
  .canvas {
    position: relative;
    width: 1200px;
    height: 900px;
  }
  .card {
    position: absolute;
    top: 100px;
    width: 450px;
    height: 700px;
    background: radial-gradient(ellipse 62% 55% at 52% 43%, var(--card-glow) 0%, var(--card-mid) 55%, var(--card-edge) 100%);
    box-shadow: 0 6px 18px rgba(0, 0, 0, 0.55);
  }
  .card--front { left: 95px; }
  .card--back { left: 660px; }

  .wordmark {
    position: absolute;
    display: flex;
    align-items: baseline;
    gap: 22px;
    font-weight: 400;
    color: var(--ink);
    white-space: nowrap;
  }
  .wordmark__name { font-size: 58px; letter-spacing: 1px; }
  .wordmark__tag { font-size: 28px; letter-spacing: 0.5px; }
  .card--front .wordmark { left: 22px; top: 308px; }
  .card--back .wordmark { left: 16px; top: 600px; }

  .accent-bar {
    position: absolute;
    left: 0;
    width: 11px;
    height: 48px;
    background: var(--ink);
  }
  .accent-bar--name { top: 180px; }
  .accent-bar--contact { top: 298px; }

  .identity, .contact {
    position: absolute;
    right: 8px;
    text-align: right;
    font-weight: 700;
  }
  .identity { top: 176px; }
  .identity__name {
    font-size: 30px;
    line-height: 34px;
    letter-spacing: 0.5px;
    text-transform: uppercase;
  }
  .identity__role {
    font-size: 18.5px;
    line-height: 20px;
    text-transform: uppercase;
  }
  .contact {
    top: 296px;
    right: 12px;
    font-size: 18px;
    line-height: 27px;
  }
</style>
</head>
<body>
  <main class="canvas">
    <section class="card card--front" aria-label="Card front">
      <div class="wordmark">
        <span class="wordmark__name">vantiri</span>
        <span class="wordmark__tag">productions</span>
      </div>
    </section>

    <section class="card card--back" aria-label="Card back">
      <span class="accent-bar accent-bar--name"></span>
      <span class="accent-bar accent-bar--contact"></span>

      <div class="identity">
        <p class="identity__name">Kenji Matsuda</p>
        <p class="identity__role">Producer/Mixer/Engineer</p>
      </div>

      <div class="contact">
        <p class="contact__phone">+81 090 4827 3516</p>
        <p class="contact__email">brightwaver@mailbox-example.com</p>
      </div>

      <div class="wordmark">
        <span class="wordmark__name">vantiri</span>
        <span class="wordmark__tag">productions</span>
      </div>
    </section>
  </main>
</body>
</html>
```